Business Card Design for Vintage Jazz

I am a vintage jazz band leader in New York City. My groups play the music of the 1920s, 1930s and 1940s. My website is marlowpeskin.com for more info on what I do.

I am looking for a two sided business card design that has the look and feel of a really nice business card from the 1930s. I need to convey with the design that my work has that vintage kind of class and style, but also conveys that we are fun and entertaining.

Most importantly it should make a bold staement. If Hollis Varnum had a card, what would it have looked like? I want a card that I feel confident will make an impact and will let people know that my work is te the top that NYC has to offer in vintage jazz..

Note that I have only decided to avoid the "committed payment" option as I have not used this service before. Assuming that I get quality work I will select a design from those presented.

Target Market(s)

people who want to hire my band for events, media, and new fans of the band

Industry/Entity Type

Performing Art

Contact Information for Business Card

Definitely a matte finish, possibly a sort of old style of paper with that brown tint? definitely a thick card.

Requirements
Must have
• FRONT
• My name: Marlow Peskin
• What I do: Bandleader, Guitarist, Vocalist, Songwriter
• Contact Details: marlowpeskin.com marlow@marlowpeskin.com 646-555-0187
• BACK
• My Social Media Links:
• facebook.marlowpeskin.com
• twitter, instagram, linkedin: marlowpeskin
• I'm also including a photo image I would like to use. The photo's background is not needed, and to be honest isn't really desireable. Just looking to use the image of me.
Nice to have
• I'm attaching which could be used as is, omitted from the card, or altered maybe with text going around the outside of the circle or in some other way. It may need some clean up to the edges of the lettering as we only use it for the website thumbnail.
• If there's space I'd like to include the text "join our mailing list for a free song download: freesong.marlowpeskin.com" If not perhaps just "Download a Free Song at: freesong.marlowpeskin.com - something to this end.
Should not have
• anything cartoony. Don't think retro 90s's vision of the swing era, think actual swing era!
• anything modern. Got to look old school
• Try to avoid dark backgrounds. Since we often play in bars and clubs where it is dar, a d
• avoid script fonts.

```html
<!DOCTYPE html>
<html lang="en">
<head>
<meta charset="utf-8">
<title>Marlow Peskin — Business Card</title>
<link rel="stylesheet" href="https://fonts.googleapis.com/css2?family=Abril+Fatface&family=Josefin+Slab:wght@400;600&display=swap">
<style>
  :root {
    --stage: #3a3837;
    --paper-light: #d8bc97;
    --paper-mid: #c7a479;
    --paper-dark: #a8845a;
    --ink: #141110;
    --portrait-dark: #1c1b1a;
    --portrait-mid: #5b5957;
    --rim: #e9dcc8;
  }
  * { box-sizing: border-box; margin: 0; padding: 0; }
  html, body { width: 1200px; height: 1200px; overflow: hidden; }
  body {
    background: var(--stage);
    display: flex;
    align-items: center;
    justify-content: center;
    gap: 60px;
  }
  .card {
    position: relative;
    width: 480px;
    height: 840px;
    background:
      radial-gradient(ellipse at 40% 35%, var(--paper-light) 0%, var(--paper-mid) 55%, var(--paper-dark) 100%);
    color: var(--ink);
  }
  .card__frame {
    position: absolute;
    inset: 26px;
    border: 3px solid var(--ink);
    border-radius: 38px;
  }
  /* Back */
  .monogram {
    position: absolute;
    top: 200px;
    left: 50%;
    transform: translateX(-50%);
    display: flex;
    flex-direction: column;
    align-items: center;
    gap: 22px;
  }
  .monogram__disc {
    width: 230px;
    height: 230px;
    border-radius: 50%;
    background: var(--ink);
  }
  .monogram__name {
    font-family: "Josefin Slab", serif;
    font-weight: 600;
    font-size: 30px;
    letter-spacing: 2px;
  }
  .social {
    position: absolute;
    top: 560px;
    left: 0;
    right: 0;
    text-align: center;
    font-family: "Josefin Slab", serif;
    font-size: 20px;
    line-height: 1.6;
  }
  /* Front */
  .identity {
    position: absolute;
    top: 58px;
    left: 0;
    right: 0;
    text-align: center;
  }
  .identity__name {
    font-family: "Abril Fatface", serif;
    font-size: 38px;
    letter-spacing: 2px;
    font-weight: 400;
  }
  .identity__role {
    font-family: "Abril Fatface", serif;
    font-size: 19px;
    margin-top: 4px;
  }
  .portrait {
    position: absolute;
    top: 200px;
    left: 50%;
    transform: translateX(-50%);
    width: 300px;
    height: 300px;
    border-radius: 50%;
    border: 3px solid var(--rim);
    background: radial-gradient(circle at 50% 40%, var(--portrait-mid) 0%, var(--portrait-dark) 70%);
  }
  .contact {
    position: absolute;
    right: 52px;
    top: 590px;
    list-style: none;
    font-family: "Josefin Slab", serif;
    font-size: 19px;
    line-height: 1.45;
    text-align: right;
  }
  .contact li { display: flex; justify-content: flex-end; align-items: center; gap: 10px; }
  .contact svg { width: 18px; height: 18px; flex: none; }
</style>
</head>
<body>
  <section class="card card--back">
    <div class="card__frame"></div>
    <div class="monogram">
      <div class="monogram__disc"></div>
      <span class="monogram__name">Marlow Peskin</span>
    </div>
    <p class="social">facebook.marlowpeskin.com<br>twitter, instagram, linkedin: marlowpeskin</p>
  </section>

  <section class="card card--front">
    <div class="card__frame"></div>
    <header class="identity">
      <h1 class="identity__name">Marlow Peskin</h1>
      <p class="identity__role">Bandleader, Guitarist, Vocalist, Songwriter</p>
    </header>
    <div class="portrait" role="img" aria-label="Black and white cut-out photo of the bandleader tipping a straw boater hat, wearing a piped blazer"></div>
    <ul class="contact">
      <li>646-555-0187
        <svg viewBox="0 0 20 20" aria-hidden="true"><path fill="#141110" d="M3 7c0-2 3-3 7-3s7 1 7 3l-3 1-1-2H7L6 8zM6 9h8l2 7H4z"/><circle cx="10" cy="12.5" r="1.8" fill="#c7a479"/></svg></li>
      <li>marlowpeskin.com
        <svg viewBox="0 0 20 20" aria-hidden="true"><rect x="2" y="5" width="16" height="11" fill="#141110"/><path d="M2 5l8 6 8-6" stroke="#c7a479" stroke-width="1.4" fill="none"/></svg></li>
      <li>marlow@marlowpeskin.com
        <svg viewBox="0 0 20 20" aria-hidden="true"><circle cx="10" cy="10" r="8" fill="#141110"/><path d="M2 10h16M10 2c3 3 3 13 0 16M10 2c-3 3-3 13 0 16" stroke="#c7a479" stroke-width="1.1" fill="none"/></svg></li>
    </ul>
  </section>
</body>
</html>
```